STAG TONIC...16oz. Aluminum Can Design needed!

We are in need of an aluminum can design for our Mineral Deer Attractant called Stag Tonic. There is nothing like it on the market. A deer attractant sold in 16oz. aluminum cans. We are looking for something eye catching. We have verbiage that needs to go on the cans. Also needs to have a UPC code on it. We will upload the 16oz. can template as well as our Product Logo and our Company Logo.

Information that needs to be on the cans:

Not For Human Consumption

Mineral Deer Attractant

Ingredients: Salt, Natural & Artificial Sweeteners, Sodium Carbonate, Calcium Carbonate, Sodium Hydroxide, Natural & Artificial Flavors, Beet Root, Sodium Benzoate.

Guaranteed Analysis:
Salt(NaCl), Min. 8.5%
Salt(NaCl), Max. 12.4%
Sodium(Na), Min. 4.0%
Sodium(Na), Max. 7.5%
Calcium(Ca), Min. 0.5%
Calcium(Ca), Max. 2.5%
Moisture, Maximum 79%

Directions: Ready to use, just pop the top and pour it out. Pour directly on the ground or over decayed stumps or logs.

Manufactured By:
Birchfall Outdoor Goods, LLC
4187 Mallory Rd.
Interlochen, MI 49218

Target Market(s)

Hunters

Industry/Entity Type

Hunting Industry

Requirements
Must have
• All the things mentioned in Project Description
Should not have
• Anything to do with Beer for Humans. This is a DEER ATTRACTANT

```html
<!DOCTYPE html>
<html lang="en">
<head>
<meta charset="utf-8">
<title>Stag Tonic – Mineral Deer Attractant Can Label</title>
<link rel="stylesheet" href="https://fonts.googleapis.com/css2?family=Archivo+Black&family=Open+Sans:wght@400;600;700&display=swap">
<style>
  :root {
    --bg: #e4e4e4;
    --label-black: #070707;
    --red: #e0202a;
    --gold: #d99a3c;
    --text-light: #e9e9e9;
    --text-muted: #bdbdbd;
    --rule: #5a5a5a;
    --upc-white: #f4f4f4;
  }
  * { box-sizing: border-box; margin: 0; padding: 0; }
  html, body { width: 1200px; height: 988px; overflow: hidden; }
  body {
    background: var(--bg);
    font-family: "Open Sans", Arial, sans-serif;
    display: flex; align-items: center; justify-content: center;
  }
  .can-label {
    width: 1120px; height: 900px;
    background: var(--label-black);
    display: grid;
    grid-template-columns: 560px 1fr;
    padding: 44px 56px 44px 36px;
    column-gap: 44px;
  }
  .front-panel {
    display: flex; flex-direction: column; align-items: center; justify-content: center;
  }
  .emblem { width: 440px; height: 314px; display: block; }
  .product-name {
    font-family: "Archivo Black", Arial, sans-serif;
    color: var(--red);
    font-size: 96px; line-height: 0.95;
    text-align: center; letter-spacing: 1px;
    margin-top: 20px;
  }
  .tagline {
    font-family: "Archivo Black", Arial, sans-serif;
    color: var(--gold);
    text-align: center; margin-top: 24px;
  }
  .tagline-top {
    display: flex; align-items: center; justify-content: center; gap: 12px;
    font-size: 30px;
  }
  .tagline-lines { display: flex; flex-direction: column; gap: 4px; width: 70px; }
  .tagline-lines span { height: 2px; background: var(--gold); display: block; }
  .tagline-bottom { font-size: 34px; letter-spacing: 1px; }
  .warning-pill {
    margin-top: 18px;
    background: var(--red);
    color: #fff;
    font-weight: 600; font-size: 17px;
    padding: 6px 20px;
    border-radius: 3px;
    letter-spacing: 0.5px;
  }
  .info-panel {
    color: var(--text-light);
    display: flex; flex-direction: column;
    padding-top: 6px;
  }
  .section-tab {
    align-self: flex-start;
    background: var(--red);
    color: #fff;
    font-weight: 700; font-size: 14px; letter-spacing: 1px;
    padding: 4px 13px;
    border-radius: 3px;
  }
  .body-text {
    font-size: 15px; line-height: 1.5;
    margin-top: 10px;
  }
  .analysis-heading {
    margin-top: 24px;
    color: var(--gold);
    font-weight: 700; font-size: 17px; letter-spacing: 1px;
  }
  .analysis-table {
    margin-top: 8px;
    width: 100%;
    border-collapse: collapse;
    font-size: 14px;
  }
  .analysis-table td {
    border: 1px solid var(--rule);
    padding: 5px 12px;
  }
  .analysis-table td:last-child { text-align: right; width: 90px; }
  .directions { margin-top: 24px; display: flex; flex-direction: column; }
  .label-footer {
    margin-top: auto;
    display: flex; align-items: flex-end; justify-content: space-between; gap: 20px;
  }
  .manufacturer {
    font-style: normal;
    font-size: 13px; line-height: 1.5;
    color: var(--text-muted);
  }
  .manufacturer-heading {
    color: var(--gold);
    font-weight: 700; font-size: 13px; letter-spacing: 1px;
    margin-bottom: 2px;
  }
  .upc-area {
    width: 150px; height: 88px;
    background: var(--upc-white);
    border-radius: 2px;
    flex-shrink: 0;
  }
</style>
</head>
<body>
  <main class="can-label">
    <section class="front-panel">
      <svg class="emblem" viewBox="0 0 420 300" role="img" aria-label="Illustration of a stag standing before pine trees and mountains on a red sun">
        <defs>
          <linearGradient id="sunGradient" x1="0" y1="0" x2="0" y2="1">
            <stop offset="0" stop-color="#e3232b"/>
            <stop offset="1" stop-color="#a9151a"/>
          </linearGradient>
        </defs>
        <path d="M40 300 A180 180 0 1 1 380 300 Z" fill="url(#sunGradient)"/>
      </svg>
      <h1 class="product-name">STAG<br>TONIC</h1>
      <div class="tagline">
        <div class="tagline-top">
          <span class="tagline-lines"><span></span><span></span><span></span></span>
          MINERAL
          <span class="tagline-lines"><span></span><span></span><span></span></span>
        </div>
        <div class="tagline-bottom">DEER ATTRACTANT</div>
      </div>
      <div class="warning-pill">• NOT FOR HUMAN CONSUMPTION •</div>
    </section>

    <section class="info-panel">
      <span class="section-tab">INGREDIENTS</span>
      <p class="body-text">Salt, Natural &amp; Artificial Sweeteners, Sodium Carbonate, Calcium Carbonate, Sodium Hydroxide, Natural &amp; Artificial Flavors, Beet Root, Sodium Benzoate.</p>

      <h2 class="analysis-heading">GUARANTEED ANALYSIS</h2>
      <table class="analysis-table">
        <tr><td>Salt(NaCl), Min.</td><td>8.5%</td></tr>
        <tr><td>Salt(NaCl), Max.</td><td>12.4%</td></tr>
        <tr><td>Sodium(Na), Min.</td><td>4.0%</td></tr>
        <tr><td>Sodium(Na), Max.</td><td>7.5%</td></tr>
        <tr><td>Calcium(Ca), Min.</td><td>0.5%</td></tr>
        <tr><td>Calcium(Ca), Max.</td><td>2.5%</td></tr>
        <tr><td>Moisture, Maximum</td><td>79%</td></tr>
      </table>

      <div class="directions">
        <span class="section-tab">DIRECTIONS</span>
        <p class="body-text">Ready to use, just pop the top and pour it out. Pour directly on the ground or over decayed stumps or logs.</p>
      </div>

      <div class="label-footer">
        <address class="manufacturer">
          <div class="manufacturer-heading">MANUFACTURED BY:</div>
          Birchfall Outdoor Goods, LLC<br>
          4187 Mallory Rd.<br>
          Interlochen, MI 49218
        </address>
        <div class="upc-area" role="img" aria-label="Space reserved for the UPC barcode"></div>
      </div>
    </section>
  </main>
</body>
</html>
```